Breezeway Comfort business cards design

Need a business card design for a Heating and Air Conditioning business. I need these items included.
Business name: Breezeway Comfort
Owner: Marcus Tollefsen
License # 2874590
Phone number # 555-382-4071
Email: breezewaycomfortair@mailvista.example
Sales
Service
Installation
Maintenance

Heating and Air Conditioning

Requirements
Must have
• Company name , license number , phone number , email

```html
<!DOCTYPE html>
<html lang="en">
<head>
<meta charset="utf-8">
<title>Breezeway Comfort — Business Cards</title>
<link rel="stylesheet" href="https://fonts.googleapis.com/css2?family=Poppins:wght@400;500;700;800&display=swap">
<style>
  :root {
    --stage: #12358a;
    --card-blue: #3456a8;
    --card-white: #f6f6f4;
    --brand-blue: #2f4fa2;
    --accent-orange: #ee8a3c;
    --accent-red: #e5475a;
    --accent-gold: #f2a51f;
    --ink-white: #ffffff;
  }
  * { margin: 0; padding: 0; box-sizing: border-box; }
  html, body { width: 1200px; height: 800px; overflow: hidden; }
  body {
    background: var(--stage);
    font-family: "Poppins", sans-serif;
    position: relative;
  }
  .card {
    position: absolute;
    top: 245px;
    width: 540px;
    height: 310px;
    overflow: hidden;
  }
  .card-front { left: 40px; border-top-right-radius: 70px; background: var(--card-white); }
  .card-back { left: 620px; border-top-left-radius: 70px; background: var(--card-blue); }

  .front-wave { position: absolute; inset: 0; }

  .front-brand {
    position: absolute; left: 52px; top: 96px;
    display: flex; align-items: center; gap: 12px;
  }
  .brand-dot {
    width: 26px; height: 26px; border-radius: 50%;
    background: var(--accent-orange);
    flex: none;
  }
  .brand-name {
    font-weight: 700; font-size: 22px; color: var(--brand-blue);
    letter-spacing: 0.5px; line-height: 1.1;
  }
  .front-brand .brand-name { display: flex; flex-direction: column; }
  .front-headline {
    position: absolute; left: 262px; top: 16px;
    font-weight: 800; font-size: 17px; letter-spacing: 0.5px;
    background: linear-gradient(90deg, var(--accent-red), var(--accent-orange));
    -webkit-background-clip: text; background-clip: text; color: transparent;
  }
  .license {
    position: absolute; left: 42px; top: 250px;
    color: var(--ink-white); line-height: 1.1;
  }
  .license-label { font-weight: 500; font-size: 12px; letter-spacing: 0.5px; }
  .license-number { font-weight: 800; font-size: 21px; color: var(--accent-gold); letter-spacing: 1px; }

  .contact { position: absolute; left: 292px; top: 158px; color: var(--ink-white); }
  .contact-name { font-weight: 800; font-size: 21px; line-height: 1.15; }
  .contact-role { font-weight: 800; font-size: 13px; color: var(--accent-orange); letter-spacing: 1.5px; margin-bottom: 12px; }
  .contact-line { display: flex; align-items: center; gap: 6px; font-size: 10px; font-weight: 400; margin-top: 4px; white-space: nowrap; }
  .contact-line svg { flex: none; }

  .back-brand {
    position: absolute; left: 0; right: 0; top: 112px;
    display: flex; justify-content: center; align-items: center; gap: 12px;
  }
  .back-brand .brand-name { color: var(--ink-white); font-size: 30px; }
  .back-brand .brand-dot { width: 34px; height: 34px; }
  .services {
    position: absolute; left: 0; right: 0; bottom: 38px;
    display: flex; justify-content: center; gap: 14px;
    list-style: none;
    font-weight: 800; font-size: 13px; letter-spacing: 0.5px; color: var(--accent-gold);
  }
  .services li { display: flex; align-items: center; gap: 14px; }
  .services li + li::before {
    content: ""; width: 7px; height: 7px; border-radius: 50%; background: var(--ink-white);
  }
</style>
</head>
<body>
  <section class="card card-front" aria-label="Business card front">
    <svg class="front-wave" viewBox="0 0 540 310" width="540" height="310" aria-hidden="true">
      <defs>
        <linearGradient id="waveStroke" x1="0" x2="1" y1="0" y2="0">
          <stop offset="0" stop-color="#e5475a"/>
          <stop offset="1" stop-color="#ee8a3c"/>
        </linearGradient>
      </defs>
      <path d="M0,242 C160,238 230,205 300,140 S440,60 540,50 L540,310 L0,310 Z" fill="#3456a8"/>
      <path d="M0,236 C160,232 230,199 300,134 S440,54 540,44" fill="none" stroke="url(#waveStroke)" stroke-width="3"/>
    </svg>

    <div class="front-brand">
      <span class="brand-dot"></span>
      <span class="brand-name"><span>Breezeway</span><span>Comfort</span></span>
    </div>

    <div class="front-headline">BREEZEWAY COMFORT</div>

    <div class="contact">
      <div class="contact-name">Marcus Tollefsen</div>
      <div class="contact-role">OWNER</div>
      <div class="contact-line">
        <svg width="12" height="12" viewBox="0 0 24 24" aria-hidden="true"><path fill="#ee8a3c" d="M6.6 10.8a15.1 15.1 0 0 0 6.6 6.6l2.2-2.2c.3-.3.7-.4 1-.2 1.1.4 2.300.6 3.6.6.6 0 1 .4 1 1V20c0 .6-.4 1-1 1A17 17 0 0 1 3 4c0-.6.4-1 1-1h3.5c.6 0 1 .4 1 1 0 1.3.2 2.5.6 3.6.1.3 0 .7-.2 1z"/></svg>
        <span>555-382-4071</span>
      </div>
      <div class="contact-line">
        <svg width="13" height="11" viewBox="0 0 26 20" aria-hidden="true"><rect x="1" y="1" width="24" height="18" rx="2" fill="none" stroke="#ee8a3c" stroke-width="2"/><path d="M1 2l12 9 12-9" fill="none" stroke="#ee8a3c" stroke-width="2"/></svg>
        <span>breezewaycomfortair@mailvista.example</span>
      </div>
    </div>

    <div class="license">
      <div class="license-label">LICENSE</div>
      <div class="license-number">2874590</div>
    </div>
  </section>

  <section class="card card-back" aria-label="Business card back">
    <div class="back-brand">
      <span class="brand-dot"></span>
      <span class="brand-name">Breezeway Comfort</span>
    </div>
    <ul class="services">
      <li>SALES</li>
      <li>SERVICE</li>
      <li>INSTALLATION</li>
      <li>MAINTENANCE</li>
    </ul>
  </section>
</body>
</html>
```